business stationery

have a gorgeous logo that needs to be incorporated on stationery. Was hoping to do something on letterhead that was a paper that looked like "bark" from a tree or something that resembled the "woods." Soft paper with some very basic natural elements. Same thing for business cards. Think American lakeside cabin. Organic. Natural. Calm and welcoming but clear to read and understand. Wanted to use alot of black.

Target Market(s)

buyers of Conrad Bellweather home. Client that would have more than one home and in need of rare pieces and items to furnish an upmarket lakeside holiday cabin in the woods. Someone who treasures beautiful hand made items, organic foods and a real crackling fire but with money to burn in it!

Industry/Entity Type

Business

Requirements
Must have
• My logo
My business name
www.thornbydell.example
Natural almost raw effect paper
My ABN: 62 730 514 907 (to be placed in small writing at the bottom of card/letterhead)
Nice to have
• The website will consist of a cabin door that you "open" with a creak sound effect and then you go "inside" to look at the various rooms to start shopping. Want to bring that element of texture and warmth into the stationary also.
Should not have
• Anything modern or hard to read items

```html
<!DOCTYPE html>
<html lang="en">
<head>
<meta charset="utf-8">
<title>Thornby Dell – Stationery</title>
<link rel="stylesheet" href="https://fonts.googleapis.com/css2?family=PT+Sans:wght@400;700&display=swap">
<style>
  :root {
    --backdrop: #808080;
    --paper: #e8dccf;
    --paper-light: #efe5da;
    --paper-dark: #dccdbd;
    --ink: #1c1a19;
    --ink-soft: #4a4440;
    --maroon: #8a2b22;
    --black: #000000;
    --white: #ffffff;
    --elk-tone: #b8a696;
    --leaf-tone: #c99a8c;
  }
  * { box-sizing: border-box; margin: 0; padding: 0; }
  html, body { width: 1200px; height: 1029px; overflow: hidden; }
  body {
    background: var(--backdrop);
    position: relative;
    font-family: "PT Sans", Arial, sans-serif;
    color: var(--ink);
  }
  .paper-texture {
    background:
      repeating-linear-gradient(88deg, rgba(255,255,255,0.08) 0 2px, rgba(0,0,0,0.025) 2px 5px),
      radial-gradient(ellipse at 30% 20%, var(--paper-light), var(--paper) 55%, var(--paper-dark));
  }

  /* Letterhead */
  .letterhead {
    position: absolute; left: 108px; top: 73px;
    width: 700px; height: 905px; overflow: hidden;
  }
  .letterhead__brand {
    position: absolute; left: 44px; top: 78px; width: 228px;
  }
  .brand-name {
    font-weight: 700; color: var(--ink); text-transform: uppercase;
    letter-spacing: 0.5px; line-height: 1; white-space: nowrap;
  }
  .letterhead__brand .brand-name { font-size: 36px; }
  .brand-byline {
    font-size: 6px; text-transform: uppercase; text-align: right;
    color: var(--maroon); margin-top: 3px; letter-spacing: 0.3px;
  }
  .letterhead__contact {
    position: absolute; right: 37px; top: 38px;
    text-align: right; font-size: 11px; line-height: 14px; color: var(--ink-soft);
  }
  .label { color: var(--maroon); }
  .letterhead__body {
    position: absolute; left: 86px; top: 230px; width: 511px;
    font-size: 11.6px; line-height: 13.6px; text-align: justify; color: var(--ink);
  }
  .letterhead__body p { margin-bottom: 13.6px; }
  .letterhead__signature {
    position: absolute; left: 81px; top: 640px; width: 111px; height: 81px;
    background: linear-gradient(135deg, rgba(28,26,25,0.0), rgba(28,26,25,0.18), rgba(28,26,25,0.0));
    border-radius: 6px;
  }
  .letterhead__decoration {
    position: absolute; left: 484px; top: 519px; width: 216px; height: 386px;
    background:
      radial-gradient(ellipse at 60% 30%, rgba(201,154,140,0.55), rgba(201,154,140,0) 60%),
      linear-gradient(180deg, rgba(184,166,150,0.15), rgba(184,166,150,0.7));
    border-top-left-radius: 120px 200px;
  }
  .letterhead__abn {
    position: absolute; left: 43px; top: 937px; font-size: 11px; color: var(--ink-soft);
  }
  .letterhead__band {
    position: absolute; left: 0; bottom: 0; width: 100%; height: 21px; background: var(--black);
  }

  /* Business cards */
  .card {
    position: absolute; left: 831px; width: 289px; height: 164px; overflow: hidden;
  }
  .card--front { top: 289px; }
  .card--back { top: 467px; height: 165px; background: var(--black); }
  .card__band {
    position: absolute; left: 0; bottom: 0; width: 100%; height: 12px; background: var(--black);
  }
  .card__person { position: absolute; right: 13px; top: 17px; text-align: right; }
  .card__name { font-size: 11.5px; font-weight: 700; color: var(--maroon); }
  .card__role { font-size: 9px; color: var(--ink-soft); margin-top: 1px; }
  .card__brand { position: absolute; left: 17px; top: 78px; width: 116px; }
  .card__brand .brand-name { font-size: 18px; }
  .card__brand .brand-byline { font-size: 4px; margin-top: 1px; }
  .card__address {
    position: absolute; right: 13px; top: 80px; text-align: right;
    font-size: 7px; line-height: 9.5px; color: var(--ink-soft);
  }
  .card__details {
    position: absolute; right: 13px; top: 110px; text-align: right;
    font-size: 7px; line-height: 9.5px; color: var(--ink-soft);
  }
  .card--back .card__logo {
    position: absolute; left: 0; right: 0; top: 78px; text-align: center;
  }
  .card--back .brand-name { color: var(--white); font-size: 30px; }
  .card--back .brand-byline { color: var(--white); font-size: 4.5px; width: 188px; margin: 2px auto 0; }
  .card__web {
    position: absolute; left: 0; right: 0; top: 122px; text-align: center;
    font-size: 10.5px; letter-spacing: 2.4px; color: var(--white);
  }
</style>
</head>
<body>

<section class="letterhead paper-texture">
  <div class="letterhead__brand">
    <div class="brand-name">Thornby Dell</div>
    <div class="brand-byline">by Wren Calloway</div>
  </div>

  <address class="letterhead__contact" style="font-style:normal">
    B2, Larchmont House,<br>
    218 Fenwick Rd, Australia 6012<br>
    <span class="label">P.</span> 6471 0820&nbsp; <span class="label">F.</span> 6471 0821<br>
    <span class="label">W.</span> www.thornbydell.example
  </address>

  <div class="letterhead__decoration" role="img" aria-label="Faint elk head silhouette with maple-leaf antlers"></div>

  <div class="letterhead__body">
    <p>Lorem ipsum dolor sit amet, consectetuer adipiscing elit. Pellentesque tristique elementum sem. Quisque eget erat ac lectus sodales faucibus. Nam commodo est. Cras consequat faucibus velit. Nam ac magna. Sed et ligula. Nam volutpat, elit ac facilisis tempor, neque augue euismod leo, sit amet molestie sem est eu libero. Nulla facilisi. Pellentesque sit amet odio. Curabitur a leo consectetuer leo blandit porttitor. Pellentesque velit quam, gravida at, pharetra eu, convallis non, sem. Aenean tempor nibh at purus. Pellentesque porta. Suspendisse congue, lacus sit amet imperdiet imperdiet, urna massa rutrum urna, id elementum tellus diam quis risus.</p>
    <p>In dui turpis, varius vitae, tincidunt id, consequat ut, leo. Donec tincidunt tristique odio. Nulla erat felis, euismod nec, fringilla non, aliquet et, magna. Nulla at magna quis nisi pretium vehicula. Pellentesque habitant morbi tristique senectus et netus et malesuada fames ac turpis egestas. Class aptent taciti sociosqu ad litora torquent per conubia nostra, per inceptos himenaeos. In vel quam. Phasellus varius convallis purus. In non turpis. Nam sed risus. Etiam non neque at nisl gravida porttitor. Donec leo dolor, feugiat ut, pharetra et, porttitor a, metus. Suspendisse laoreet magna vel elit. Ut est augue, fermentum ac, molestie at, vestibulum et, urna.</p>
    <p>Nunc purus. Cras auctor. In ornare neque id ipsum. Nulla tincidunt, diam sit amet viverra euismod, sapien augue fringilla neque, at pellentesque felis tortor vel enim. Etiam dignissim. Sed a tortor vel nisl euismod ultricies. Donec molestie congue lectus. Integer sed turpis a tortor imperdiet consequat. Maecenas molestie placerat urna. Sed pede enim, sollicitudin nec, pretium nec, sollicitudin a, felis. In hac habitasse platea dictumst. Nam facilisis, tellus non scelerisque placerat, turpis turpis semper ante, euismod imperdiet augue nisi et neque. Vivamus tincidunt.</p>
    <p>Nulla lobortis ultricies nulla. Pellentesque purus mi, consequat quis, hendrerit sed, imperdiet non, eros. Nullam urna est, vehicula nec, cursus nec, dignissim sit amet, risus. Duis molestie, tellus sit amet laoreet ullamcorper, urna nisi fringilla ante, at rhoncus justo dolor vel dui. Nam hendrerit luctus lorem. Aenean tempor, metus vel posuere gravida, arcu nunc imperdiet tellus, ut blandit sem magna a turpis. Vivamus in neque. Lorem ipsum dolor sit amet, consectetuer adipiscing.</p>
  </div>

  <div class="letterhead__signature" role="img" aria-label="Handwritten signature"></div>

  <div class="letterhead__abn"><span class="label">ABN.</span> 62 730 514 907</div>
  <div class="letterhead__band"></div>
</section>

<section class="card card--front paper-texture">
  <div class="card__person">
    <div class="card__name">Owen Marsh</div>
    <div class="card__role">Marketing Manager</div>
  </div>
  <div class="card__brand">
    <div class="brand-name">Thornby Dell</div>
    <div class="brand-byline">by Wren Calloway</div>
  </div>
  <div class="card__address">
    B2, Larchmont House, 218 Fenwick Rd,<br>
    KESTREL VALE West Australia 6012
  </div>
  <div class="card__details">
    <span class="label">phone.</span> (41) 32-5170446<br>
    <span class="label">fax.</span> (41) 32-5170446<br>
    <span class="label">email.</span> info@thornbydell.example<br>
    <span class="label">ABN.</span> 62 730 514 907
  </div>
  <div class="card__band"></div>
</section>

<section class="card card--back">
  <div class="card__logo">
    <div class="brand-name">Thornby Dell</div>
    <div class="brand-byline">by Wren Calloway</div>
  </div>
  <div class="card__web">www.thornbydell.example</div>
</section>

</body>
</html>
```